BROCHURE VELNORA

I HAVE TO REORGANIZE THE ATTACHED BROCHURE

Target Market(s)

FACTORY USE

Industry/Entity Type

MEDICAL COSMETIC

Font styles to use
Serif

Colors
0054AA
0677BA
7BADD7
CADEEF
E8F1F8

Requirements
Must have
• I need only reorganize the brochure

```html
<!DOCTYPE html>
<html lang="it">
<head>
<meta charset="utf-8">
<title>Velnora – Formazione Tricologica</title>
<link href="https://fonts.googleapis.com/css2?family=Comfortaa:wght@400;600;700&display=swap" rel="stylesheet">
<style>
  :root{
    --navy:#0054AA;
    --blue:#0677BA;
    --sky:#2aa6df;
    --pale:#CADEEF;
    --mist:#E8F1F8;
    --ink:#3d4652;
    --grey:#8a8f96;
    --sorter:#e6e6e6;
  }
  *{box-sizing:border-box;margin:0;padding:0}
  html,body{width:1200px;height:635px;overflow:hidden;background:var(--sorter)}
  body{position:relative;font-family:'Comfortaa',sans-serif;color:var(--ink)}

  .slide{position:absolute;width:377px;height:283px;overflow:hidden;
    background:linear-gradient(to bottom,#fff 0%,#fff 72%,#eef0f2 86%,#dfe2e5 100%);
    box-shadow:0 0 0 1px #cfcfcf}
  .slide-num{position:absolute;font-size:11px;color:#555}
  .slide > *{position:absolute}

  .footer-mark{left:4px;top:276px;font-size:5px;color:var(--grey)}
  .page-no{right:5px;top:275px;font-size:5.5px;color:var(--grey)}

  .mini-brand{right:8px;top:7px;display:flex;align-items:center;gap:2px;
    font-size:8px;font-weight:700;color:var(--navy)}
  .mini-brand i{width:6px;height:6px;background:var(--sky);display:block}
  .mini-brand + .mini-rule{right:8px;top:20px;width:46px;height:1px;background:var(--sky);opacity:.6}

  /* slide 1 */
  .brand{left:0;width:100%;top:33px;display:flex;justify-content:center;align-items:center;gap:6px;
    font-size:27px;font-weight:700;color:var(--navy)}
  .brand i{width:20px;height:20px;background:var(--sky);display:block}
  .brand-tag{left:0;width:100%;top:72px;text-align:center;font-size:6.5px;color:var(--navy);letter-spacing:.2px}
  .cover-title{left:0;width:100%;top:120px;text-align:center;font-size:32px;font-weight:700;
    color:var(--navy);line-height:42px;letter-spacing:.5px}
  .cover-sub{left:0;width:100%;top:208px;text-align:center;font-size:13px;color:var(--sky);letter-spacing:.4px}

  /* slide 2 */
  .herb-photo{left:0;top:0;width:189px;height:283px;
    background:linear-gradient(135deg,#8a8f88 0%,#6f7a62 35%,#dadbd6 60%,#7f8a6c 85%,#5c5f58 100%)}
  .section-title{left:189px;width:188px;text-align:center;color:var(--navy);font-size:23px;line-height:34px;top:76px}
  .section-sub{left:189px;width:188px;text-align:center;color:var(--sky);font-size:16px;line-height:28px;top:159px}

  /* index slides */
  .index-title{left:44px;font-size:18px;color:var(--sky);letter-spacing:.3px}
  .title-rule{left:0;height:1.5px;background:var(--navy)}
  .intro-head{left:43px;top:72px;font-size:14px;color:var(--navy)}
  .intro-text{left:64px;top:91px;font-size:11px;line-height:14px;color:var(--ink)}
  .intro-text small{font-size:8.5px;color:var(--grey)}
  .intro-note{left:64px;top:121px;font-size:8.5px;line-height:12.5px;color:var(--grey)}
  .topic{left:50px;display:flex;align-items:center;gap:5px;font-size:11.5px;color:var(--ink);white-space:nowrap}
  .topic b{font-weight:400;width:16px;height:16px;border:1px solid var(--sky);border-radius:50%;
    display:flex;align-items:center;justify-content:center;font-size:10px;color:var(--sky);margin-left:-8px}
  .topic em{font-style:normal;color:var(--grey)}
  .topic-note{left:65px;font-size:8.5px;color:var(--grey)}
  .topic-note.strong{font-size:11px;color:var(--ink)}
  .sub-list{left:87px;top:212px;list-style:none;font-size:8.5px;line-height:12.8px;color:var(--grey)}
  .sub-list li::before{content:"▪";margin-right:3px;font-size:6px;vertical-align:1px}

  /* slide 5 */
  .chapter{left:0;width:377px;text-align:center;top:114px;font-size:17px;color:var(--navy)}
  .chapter-sub{left:0;width:377px;text-align:center;top:156px;font-size:16px;color:var(--sky)}

  /* slide 6 */
  .skin-illustration{left:113px;top:56px;width:161px;height:200px;border-radius:4px;
    background:linear-gradient(160deg,#f3c7cf 0%,#e89aab 45%,#f4d3a6 80%,#f0b8c2 100%)}
  .callouts{left:0;top:0;width:377px;height:283px}
  .callouts text{font-family:'Comfortaa',sans-serif;font-size:6px;fill:var(--navy)}
</style>
</head>
<body>

<!-- slide 1 -->
<section class="slide" style="left:5px;top:5px">
  <div class="brand"><i></i>Velnora</div>
  <div class="brand-tag">CURA E REINTEGRAZIONE DEI CAPELLI</div>
  <h1 class="cover-title">1° FORMAZIONE<br>TRICOLOGICA</h1>
  <p class="cover-sub">Dei Tecnici Tricologi Interni</p>
  <span class="footer-mark">© Velnora</span>
</section>
<span class="slide-num" style="left:5px;top:294px">1</span>

<!-- slide 2 -->
<section class="slide" style="left:411px;top:5px">
  <div class="herb-photo" role="img" aria-label="Mortaio bianco con erbe aromatiche fresche su tavolo di legno"></div>
  <div class="mini-brand"><i></i>Velnora</div><div class="mini-rule"></div>
  <h2 class="section-title">PRINCIPALI<br>ANOMALIE</h2>
  <p class="section-sub">DEL CUOIO<br>CAPELLUTO</p>
  <span class="page-no">2</span>
</section>
<span class="slide-num" style="left:411px;top:294px">2</span>

<!-- slide 3 -->
<section class="slide" style="left:817px;top:5px">
  <div class="mini-brand"><i></i>Velnora</div><div class="mini-rule"></div>
  <h2 class="index-title" style="top:37px">INDICE DEGLI ARGOMENTI</h2>
  <div class="title-rule" style="top:58px;width:215px"></div>
  <p class="intro-head">Introduzione:</p>
  <p class="intro-text">GENERALITA' TRICOLOGICHE e<br>L'INTOSSINAZIONE <small>ovvero l'origine</small></p>
  <p class="intro-note" style="top:119px">di tutte le anomalie fisiologiche e<br>cutanee.</p>
  <p class="topic" style="top:157px"><b>1</b>EFFLUVIO IN TELOGEN <em>(TEA e TEC)</em></p>
  <p class="topic" style="top:184px"><b>2</b>GHIANDOLA SEBACEA DISFUNZIONALE</p>
  <p class="topic" style="top:213px"><b>3</b>PITYRIASIS CAPITIS – LA FORFORA:</p>
  <p class="topic-note" style="top:229px">Sue diverse forme e trattamenti proposti</p>
  <p class="topic" style="top:253px"><b>4</b>DERMATITI, DERMATOSI.</p>
  <span class="footer-mark">© Velnora</span>
  <span class="page-no">3</span>
</section>
<span class="slide-num" style="left:817px;top:294px">3</span>

<!-- slide 4 -->
<section class="slide" style="left:5px;top:329px">
  <div class="mini-brand"><i></i>Velnora</div><div class="mini-rule"></div>
  <h2 class="index-title" style="top:37px">INDICE DEGLI ARGOMENTI</h2>
  <div class="title-rule" style="top:57px;width:253px"></div>
  <p class="topic" style="top:73px"><b>5</b>PSORIASI, DERMATITE PSICOGENA</p>
  <p class="topic" style="top:110px"><b>6</b>ALOPECIA PSORISIACA</p>
  <p class="topic" style="top:146px"><b>7</b>RED BURNED SKIN DISEASE</p>
  <p class="topic-note strong" style="top:163px">Effluvio in telogen</p>
  <p class="topic" style="top:192px"><b>8</b>PARASSITOSI:</p>
  <ul class="sub-list">
    <li>PEDICULOSI</li>
    <li>PIATTOLE</li>
    <li>PIDOCCHIO DEL CORPO.</li>
    <li>DEMODEX, DEMODECIDOSI.</li>
  </ul>
  <span class="footer-mark">© Velnora</span>
  <span class="page-no">4</span>
</section>
<span class="slide-num" style="left:5px;top:618px">4</span>

<!-- slide 5 -->
<section class="slide" style="left:411px;top:329px">
  <div class="mini-brand"><i></i>Velnora</div><div class="mini-rule"></div>
  <h2 class="chapter">La Salute Del Cuoio Capelluto</h2>
  <div class="title-rule" style="top:139px;width:237px"></div>
  <p class="chapter-sub">FONDAMENTI</p>
  <span class="footer-mark">© Velnora</span>
  <span class="page-no">5</span>
</section>
<span class="slide-num" style="left:411px;top:618px">5</span>

<!-- slide 6 -->
<section class="slide" style="left:817px;top:329px">
  <div class="mini-brand"><i></i>Velnora</div><div class="mini-rule"></div>
  <h2 class="index-title" style="left:41px;top:25px">IL CUOIO CAPELLUTO</h2>
  <div class="title-rule" style="top:45px;width:215px"></div>
  <div class="skin-illustration" role="img" aria-label="Sezione anatomica della pelle del cuoio capelluto con follicoli, ghiandole e capillari"></div>
  <svg class="callouts" viewBox="0 0 377 283" aria-hidden="true">
    <g stroke="#2aa6df" stroke-width=".8" fill="none">
      <line x1="20" y1="165" x2="150" y2="165"/>
      <line x1="20" y1="182" x2="162" y2="182"/>
      <line x1="20" y1="204" x2="125" y2="204"/>
      <line x1="20" y1="222" x2="170" y2="222"/>
      <line x1="355" y1="151" x2="236" y2="151"/>
      <line x1="355" y1="204" x2="228" y2="204"/>
      <line x1="355" y1="217" x2="220" y2="217"/>
    </g>
    <text x="20" y="163">CANALE LINFATICO</text>
    <text x="20" y="180">GHIANDOLA SEBACEA</text>
    <text x="20" y="202">GHIANDOLA SUDORALE</text>
    <text x="20" y="220">CAPILLARE ARTERIOSO</text>
    <text x="355" y="149" text-anchor="end">MUSCOLO ERETTORE</text>
    <text x="355" y="202" text-anchor="end">PAPILLA GERMINATIVA</text>
    <text x="355" y="215" text-anchor="end">CAPILLARE VENOSO</text>
  </svg>
  <span class="footer-mark">© Velnora</span>
  <span class="page-no">6</span>
</section>
<span class="slide-num" style="left:817px;top:618px">6</span>

</body>
</html>
```